Shopify Web-Page "Tovi-BrambleDays

We are building a new business in Switzerland offering premium sewing holiday camps for kids aged 9–14. In enclosed brief outlines our requirements for a complete Shopify homepage design and a multilingual logo creation.
Domains: tovi-brambledays.ch ; tovi-giornirovo.ch ; tovi-brombeertage.ch

Project Overview
We are looking for:
1. A modern, fully designed Shopify homepage in English using standard Shopify content blocks (no custom coding), which we can later update ourselves. Supporting Multilanguage (EN, German, Italian).

2. A logo design that includes the brand identity and communicates our multilingual, creative, and child-focused positioning.

All details in enclosed

```html
<!DOCTYPE html>
<html lang="en">
<head>
<meta charset="utf-8">
<title>Tovi BrambleDays – Sewing Camps for Kids</title>
<link href="https://fonts.googleapis.com/css2?family=Figtree:wght@400;500;600;700&family=Space+Mono&display=swap" rel="stylesheet">
<style>
:root{
  --cream:#fdf9f2;
  --orange:#e8704a;
  --ink:#1f3b40;
  --teal:#3c7a78;
  --peach:#fbe6d3;
  --navy:#16163a;
  --muted:#5b6b6e;
  --line:#ece4d8;
}
*{margin:0;padding:0;box-sizing:border-box}
html,body{width:1200px;height:4669px;overflow:hidden}
body{background:var(--cream);font-family:"Figtree",sans-serif;color:var(--ink);position:relative}
.abs{position:absolute}
.wordmark{font-family:"Figtree",sans-serif;font-weight:600;text-align:center;white-space:nowrap;line-height:1}
.logo-hero{left:0;width:1200px;top:270px;color:var(--orange);font-size:72px}
.variant{top:690px;width:320px;font-size:34px}
.band{left:0;top:990px;width:1200px;height:123px;background:var(--orange)}
.badge{left:455px;top:1018px;width:290px;height:200px;border-radius:50%;background:var(--cream);border:7px solid var(--orange);display:flex;align-items:center;justify-content:center;color:var(--orange);font-size:32px}
.hero-title{left:123px;top:1198px;font-size:44px;font-weight:500;line-height:1.3}
.hero-lead{left:113px;top:1318px;width:530px;font-size:21px;font-weight:500;color:var(--teal);line-height:1.3}
.hero-copy{left:113px;width:530px;font-size:12.5px;color:var(--teal);line-height:1.35}
.photo{border-radius:18px}
.hero-photo{left:680px;top:1167px;width:402px;height:418px;background:linear-gradient(135deg,#e9ddd0,#c9a98f 45%,#5f97c4 80%,#e8d5c4)}
.btn{background:var(--orange);color:#fff;font-weight:500;display:flex;align-items:center;justify-content:center}
.hero-btn{left:121px;top:1586px;width:249px;height:64px;font-size:27px}
.section-title{left:0;width:1200px;text-align:center;font-size:41px;font-weight:500}
.step{width:240px;text-align:center}
.circle{width:152px;height:152px;border-radius:50%;background:var(--peach);margin:0 auto;display:flex;align-items:center;justify-content:center}
.step h3{font-size:20px;font-weight:500;margin-top:22px}
.step p{font-size:9.5px;line-height:1.25;margin-top:8px}
.arrow{top:1828px;width:40px;height:10px}
.why{top:2168px;width:260px;text-align:center}
.why .circle{width:140px;height:140px}
.why h3{font-size:20px;font-weight:500;line-height:1.5;margin-top:8px}
.why p{font-size:16px;color:var(--teal)}
.card{top:2692px;width:298px}
.card .photo{height:218px;border-radius:12px}
.card h3{font-size:30px;font-weight:500;margin:28px 0 0 16px}
.card .yr{font-size:24px;color:var(--muted);margin:8px 0 0 16px}
.card .btn{margin:18px 0 0 16px;width:182px;height:47px;border-radius:6px;font-size:20px}
.quote{top:3258px;width:430px;font-size:25px;line-height:1.6;color:#2b3436}
.quote b{display:block;font-size:22px;font-weight:600;margin-top:14px}
.dot{top:3547px;width:12px;height:12px;border-radius:50%;background:var(--orange)}
.faq-row{position:absolute;left:0;width:440px;font-size:16.5px;font-weight:500;line-height:1.6;border-bottom:1px solid var(--line);padding-bottom:10px;padding-right:70px}
.plus{position:absolute;right:0;top:50%;transform:translateY(-60%);width:50px;height:50px;border-radius:50%;background:var(--peach);color:var(--orange);font-size:36px;display:flex;align-items:center;justify-content:center}
.footer{left:0;top:4298px;width:1200px;height:371px;background:var(--navy)}
.signup{left:70px;top:4343px;font-size:28px;color:var(--orange);line-height:1.22}
.email{left:70px;top:4472px;width:424px;border-bottom:1px solid var(--orange);font-family:"Space Mono",monospace;font-size:12px;color:var(--orange);padding-bottom:10px}
.social{top:4522px;width:26px;height:26px;border-radius:50%;background:var(--orange)}
.links{top:4346px;font-size:9.5px;color:var(--orange);line-height:2.6;text-transform:uppercase}
.copy{left:70px;top:4588px;font-size:9px;color:var(--orange)}
.currency{left:818px;top:4621px;width:310px;height:24px;background:var(--orange);color:var(--navy);font-size:11px;padding:5px 8px}
</style>
</head>
<body>

<div class="abs wordmark logo-hero">Tovi BrambleDays</div>

<div class="abs wordmark variant" style="left:95px;color:#111">Tovi BrambleDays</div>
<div class="abs wordmark variant" style="left:440px;color:var(--orange)">Tovi BrambleDays</div>
<div class="abs wordmark variant" style="left:790px;color:var(--teal)">Tovi BrambleDays</div>

<div class="abs band"></div>
<div class="abs wordmark badge">Tovi BrambleDays</div>

<h1 class="abs hero-title">Sew, Create,<br>and Shine!</h1>
<p class="abs hero-lead">At Tovi BrambleDays, creativity and confidence come together.</p>
<p class="abs hero-copy" style="top:1384px">Guided by Lena and Mara, who bring over 10 years of experience in teaching children sewing, tailoring, and design, our camps blend fun, style, and structure in a warm, encouraging environment.</p>
<p class="abs hero-copy" style="top:1452px">In small groups of up to 8 children, we guide young talents through a joyful week of creativity – with real results: self-sewn pieces, new friends, and a lot of pride.</p>
<p class="abs hero-copy" style="top:1520px">On the final day, the children take the spotlight in a friendly fashion show, presenting their very own handmade creations – a moment full of smiles, applause, and confidence!</p>
<div class="abs photo hero-photo" role="img" aria-label="A mother and daughter sewing together at a sewing machine"></div>
<a class="abs btn hero-btn">Book your camp</a>

<h2 class="abs section-title" style="top:1665px">How the Camp Works</h2>

<div class="abs step" style="left:119px;top:1759px">
  <div class="circle"><svg width="70" height="70" viewBox="0 0 70 70"><rect x="18" y="10" width="34" height="8" rx="2" fill="#1f3b40"/><rect x="22" y="18" width="26" height="34" fill="#e8704a"/><rect x="18" y="52" width="34" height="8" rx="2" fill="#1f3b40"/><path d="M48 30 q14 4 6 16" stroke="#e8704a" stroke-width="3" fill="none"/></svg></div>
  <h3>Project Selection</h3><p>Your child chooses<br>their own model based on previously produced<br>clothing items and sewing patterns.</p>
</div>
<svg class="abs arrow" style="left:340px" viewBox="0 0 40 10"><path d="M2 5h34M30 1l6 4-6 4" stroke="#e8704a" stroke-width="1.5" fill="none"/></svg>
<div class="abs step" style="left:360px;top:1759px">
  <div class="circle"><svg width="70" height="70" viewBox="0 0 70 70"><path d="M14 14h36v40H14z" fill="#3c7a78"/><circle cx="50" cy="34" r="12" fill="#8fb8b3"/><rect x="14" y="48" width="38" height="8" fill="#d5e4de"/></svg></div>
  <h3>Fabric Choice</h3><p>High-quality fabrics are available.</p>
</div>
<svg class="abs arrow" style="left:580px" viewBox="0 0 40 10"><path d="M2 5h34M30 1l6 4-6 4" stroke="#e8704a" stroke-width="1.5" fill="none"/></svg>
<div class="abs step" style="left:600px;top:1759px">
  <div class="circle"><svg width="76" height="70" viewBox="0 0 76 70"><path d="M8 20h52v14H40v16H28V34H8z" fill="#e8704a"/><rect x="4" y="50" width="64" height="8" fill="#e8704a"/><circle cx="56" cy="27" r="4" fill="#fbe6d3"/></svg></div>
  <h3>Learn &amp; Sew</h3><p>Learn how to use a sewing machine</p>
</div>
<svg class="abs arrow" style="left:820px" viewBox="0 0 40 10"><path d="M2 5h34M30 1l6 4-6 4" stroke="#e8704a" stroke-width="1.5" fill="none"/></svg>
<div class="abs step" style="left:839px;top:1759px">
  <div class="circle"><svg width="74" height="74" viewBox="0 0 24 24"><path d="M12 2l3 6.5 7 .8-5.2 4.8 1.5 7L12 17.5 5.7 21l1.5-7L2 9.3l7-.8z" fill="#e8704a"/></svg></div>
  <h3>Showtime!</h3><p>Fashion show or photo shoot<br>at the end of the week</p>
</div>

<h2 class="abs section-title" style="top:2092px">Why Parents Choose Us</h2>

<div class="abs why" style="left:102px">
  <div class="circle"><svg width="80" height="70" viewBox="0 0 80 70"><circle cx="40" cy="14" r="8" fill="#e8704a"/><circle cx="20" cy="20" r="7" fill="#e8704a"/><circle cx="60" cy="20" r="7" fill="#e8704a"/><rect x="30" y="26" width="20" height="34" rx="5" fill="#e8704a"/><rect x="11" y="31" width="18" height="29" rx="5" fill="#e8704a"/><rect x="51" y="31" width="18" height="29" rx="5" fill="#e8704a"/></svg></div>
  <h3>Small groups</h3><p>&amp;<br>personalized attention</p>
</div>
<div class="abs why" style="left:343px">
  <div class="circle"><svg width="100" height="60" viewBox="0 0 100 60"><circle cx="30" cy="30" r="24" fill="#e8704a"/><text x="30" y="40" font-size="28" font-family="Figtree,sans-serif" font-weight="700" fill="#fff" text-anchor="middle">A</text><circle cx="68" cy="30" r="24" fill="#e8704a"/><path d="M58 22h20M68 18v4M60 42c6-6 10-12 12-20M64 30c4 6 8 10 12 12" stroke="#fff" stroke-width="3" fill="none"/></svg></div>
  <h3>Multilingual<br>supervision</h3><p>(DE / EN / IT)</p>
</div>
<div class="abs why" style="left:590px">
  <div class="circle"><svg width="70" height="80" viewBox="0 0 70 80"><circle cx="35" cy="30" r="24" fill="none" stroke="#e8704a" stroke-width="5"/><path d="M24 30l8 8 14-16" stroke="#e8704a" stroke-width="5" fill="none"/><path d="M20 50l-8 22 12-4 6 10 6-18M50 50l8 22-12-4-6 10-6-18" fill="#e8704a"/></svg></div>
  <h3>Premium matial<br>&amp; sewing machines</h3><p>(Swiss-made)</p>
</div>
<div class="abs why" style="left:836px">
  <div class="circle"><svg width="80" height="80" viewBox="0 0 80 80"><circle cx="40" cy="30" r="20" fill="none" stroke="#e8704a" stroke-width="4"/><path d="M20 30h40M40 10c-10 12-10 28 0 40M40 10c10 12 10 28 0 40" stroke="#e8704a" stroke-width="3" fill="none"/><path d="M8 44l14 22h16M72 44L58 66H42" stroke="#e8704a" stroke-width="5" fill="none"/></svg></div>
  <h3>Safe, loving<br>environment</h3><p>in Zurich</p>
</div>

<h2 class="abs section-title" style="top:2484px">Upcoming Sewing Camps</h2>
<h2 class="abs" style="left:122px;top:2608px;font-size:36px;font-weight:600">Find Your Next Sewing Adventure!</h2>

<div class="abs card" style="left:118px">
  <div class="photo" role="img" aria-label="A girl sewing fabric at a white sewing machine" style="background:linear-gradient(135deg,#e8dfd3,#d9a79a 50%,#b8c7d6)"></div>
  <h3>Spring Camps</h3><p class="yr">2026</p><a class="btn">Book Now →</a>
</div>
<div class="abs card" style="left:448px;width:302px">
  <div class="photo" role="img" aria-label="Two girls working together with colourful fabric" style="background:linear-gradient(135deg,#e2d3c3,#d7a592 45%,#3b8fb4)"></div>
  <h3>Summer Camps</h3><p class="yr">2026</p><a class="btn">Book Now →</a>
</div>
<div class="abs card" style="left:782px">
  <div class="photo" role="img" aria-label="A girl in a yellow shirt sewing at a machine" style="background:linear-gradient(135deg,#e9e4dc,#b98a6c 45%,#e7a321)"></div>
  <h3>Autumn Camps</h3><p class="yr">2026</p><a class="btn">Book Now →</a>
</div>

<h2 class="abs" style="left:122px;top:3168px;font-size:38px;font-weight:600">Parents Say...</h2>
<p class="abs quote" style="left:123px">“My doughter absolutely loiveed it! She came home proud of her handmade skirt and can’t wait for the next camp.”<b>Anja, Zurich</b></p>
<p class="abs quote" style="left:636px">“A wonderful experience • The team is caring and organized, and the kids truly shine.”<b>Luca, Zug</b></p>
<div class="abs dot" style="left:576px"></div><div class="abs dot" style="left:594px"></div><div class="abs dot" style="left:612px"></div>

<h2 class="abs" style="left:115px;top:3694px;font-size:44px;font-weight:500">FAQ</h2>
<div class="abs" style="left:115px;top:0">
  <div class="faq-row" style="top:3780px;padding-right:170px">Does my child need prior sewing experience?<span class="plus">+</span></div>
  <div class="faq-row" style="top:3866px">What materials are provided?<span class="plus">+</span></div>
  <div class="faq-row" style="top:3922px">How many items will my child make?<span class="plus">+</span></div>
  <div class="faq-row" style="top:3980px">Where do the camps take place?<span class="plus">+</span></div>
  <div class="faq-row" style="top:4040px">Do you offer a pick-up service?<span class="plus">+</span></div>
</div>
<div class="abs" style="left:656px;top:0">
  <div class="faq-row" style="top:3810px">Are the camps multilingual?<span class="plus">+</span></div>
  <div class="faq-row" style="top:3866px">What’s the maximum group size?<span class="plus">+</span></div>
  <div class="faq-row" style="top:3920px">Is lunch included?<span class="plus">+</span></div>
  <div class="faq-row" style="top:3974px">Can parents attend the final day?<span class="plus">+</span></div>
  <div class="faq-row" style="top:4027px">How do I register?<span class="plus">+</span></div>
</div>

<div class="abs wordmark" style="left:450px;width:300px;top:4232px;font-size:20px;color:var(--orange)">Tovi BrambleDays</div>

<footer class="abs footer"></footer>
<p class="abs signup">We bake emails too.<br>Sign up to receive the<br>latest news.</p>
<div class="abs email">Email Address<svg style="position:absolute;right:0;top:0" width="18" height="18" viewBox="0 0 18 18"><circle cx="9" cy="9" r="9" fill="#e8704a"/><path d="M5 9h7M9 6l3 3-3 3" stroke="#16163a" stroke-width="1.6" fill="none"/></svg></div>
<div class="abs social" style="left:70px"></div>
<div class="abs social" style="left:116px"></div>
<div class="abs social" style="left:162px"></div>
<div class="abs social" style="left:208px"></div>
<div class="abs links" style="left:711px">Get in touch<br>Join our team<br>About<br>FAQ<br>Terms of use<br>Privacy</div>
<div class="abs links" style="left:945px">Cookie club<br>Merch<br>Terms of service<br>Give $15, get $15<br>Shipping<br>California CCPA</div>
<p class="abs copy">Tovi BrambleDays All Rights Reserved 2025</p>
<div class="abs currency">United States (USD $)<span style="float:right">⌄</span></div>
<svg class="abs" style="left:1155px;top:4622px" width="22" height="24" viewBox="0 0 22 24"><circle cx="11" cy="4" r="3" fill="#e8704a"/><path d="M3 9h16M11 9v7l-5 7M11 16l5 7" stroke="#e8704a" stroke-width="2.5" fill="none"/></svg>

</body>
</html>
```